Tasman Curdworks Guild needs new business cards

We need new business cards designed and produced. We are likely to need other design work done for ads, flyers etc in future.

We would like to start with an initial business card.

The Tasman Curdworks Guild (TCG) is a membership-based not-for-profit organisation that looks after the interests of Australia's small to medium artisan cheesemakers, many of whom are also small-scale farmers. The design should be simple, using our logo, but also communicate our artisan cheese and small dairy farm focus.

The first card to be designed and produced is for me, Miriam Tolhurst. My details are:

Miriam Tolhurst
Secretary
Tasman Curdworks Guild (TCG)
http://www.curdworksguild.example
T +61452837190
E miriam.miriamtolhurst@mailbox.example

I have attached the TCG logo in jpg form. I have a higher resolution version available if needed.

Thank you!

Miriam

Miriam Tolhurst
Tasman Curdworks Guild
miriam.miriamtolhurst@mailbox.example
+61452837190

Sans Serif

• Logo (see attached file)

```html
<!DOCTYPE html>
<html lang="en">
<head>
<meta charset="utf-8">
<title>Tasman Curdworks Guild – Business Card</title>
<link rel="stylesheet" href="https://fonts.googleapis.com/css2?family=Open+Sans:wght@400;600&display=swap">
<style>
  :root {
    --backdrop: #e4e6e9;
    --card: #fbfbf9;
    --brown: #6e4320;
    --gold: #e2a43c;
    --ink: #1f1f1f;
    --shadow: rgba(40, 50, 70, 0.22);
  }
  html, body {
    margin: 0;
    width: 1200px;
    height: 854px;
    overflow: hidden;
    background: var(--backdrop);
    font-family: "Open Sans", Arial, sans-serif;
  }
  .business-card {
    position: absolute;
    left: 150px;
    top: 170px;
    width: 900px;
    height: 514px;
    background: var(--card);
    box-shadow: 0 10px 30px var(--shadow);
  }
  .brand {
    position: absolute;
    left: 520px;
    top: 62px;
    display: flex;
    align-items: center;
    gap: 22px;
  }
  .brand-dot {
    width: 74px;
    height: 74px;
    border-radius: 50%;
    background: var(--gold);
    flex: none;
  }
  .brand-name {
    margin: 0;
    color: var(--brown);
    font-weight: 400;
    font-size: 24px;
    line-height: 1.12;
  }
  .contact-block {
    position: absolute;
    left: 72px;
    top: 290px;
  }
  .person-name {
    margin: 0;
    color: var(--brown);
    font-weight: 400;
    font-size: 34px;
    letter-spacing: 0.5px;
    text-transform: uppercase;
    line-height: 1.1;
  }
  .person-role {
    margin: 2px 0 22px;
    color: var(--gold);
    font-size: 23px;
    letter-spacing: 0.5px;
    text-transform: uppercase;
  }
  .contact-list {
    list-style: none;
    margin: 0;
    padding: 0;
    color: var(--ink);
    font-size: 22px;
    line-height: 1.55;
  }
  .contact-label {
    color: var(--brown);
  }
</style>
</head>
<body>
  <main class="business-card">
    <div class="brand">
      <span class="brand-dot" aria-hidden="true"></span>
      <p class="brand-name">Tasman<br>Curdworks<br>Guild</p>
    </div>

    <section class="contact-block">
      <h1 class="person-name">Miriam Tolhurst</h1>
      <p class="person-role">Secretary</p>
      <ul class="contact-list">
        <li><span class="contact-label">P :</span> + 614 528 37190</li>
        <li>miriam.miriamtolhurst@mailbox.example</li>
        <li>www.curdworksguild.example</li>
      </ul>
    </section>
  </main>
</body>
</html>
```